Plumbing Company After Business Card

Business card for a plumbing business that offers a variety of plumbing services including maintenance, domestic and commercial plumbing. My main focus is to offer high quality professional service. A logo on the card would be ideal. Any other questions feel free to email. Cheers

Looking for something modern and upmarket with preferably a matte black background

Business name is Keystone Plumbing and Gas

Industry/Entity Type

Plumbing

Contact Information for Business Card

Keystone Plumbing and Gas
Marcus Thornell
0427915368
14 Corrigan Road, Elmvale 3561
keystoneplumbing@mailbay.com.au
ABN 52 647 183 925

Font styles to use
Sans Serif

Colors
1b1b1b
ffffff
3377b5

Requirements
Must have
• Domestic
• Commercial
• Maintenance

```html
<!DOCTYPE html>
<html lang="en">
<head>
<meta charset="utf-8">
<title>Keystone Plumbing and Gas – Business Card</title>
<link rel="stylesheet" href="https://fonts.googleapis.com/css2?family=Jost:wght@300;400;600;700&display=swap">
<style>
  :root {
    --card-black: #000000;
    --wave-blue: #006aa3;
    --mark-blue: #3377b5;
    --brand-red: #e8232f;
    --text-white: #ffffff;
    --font-main: "Jost", sans-serif;
  }
  html, body {
    margin: 0;
    padding: 0;
    overflow: hidden;
    background: var(--card-black);
  }
  .card {
    position: relative;
    width: 1200px;
    height: 741px;
    background: var(--card-black);
    overflow: hidden;
    font-family: var(--font-main);
    color: var(--text-white);
  }
  .card__wave {
    position: absolute;
    inset: 0;
    width: 1200px;
    height: 741px;
  }
  .card__wave path { fill: var(--wave-blue); }

  .brand-mark {
    position: absolute;
    left: 232px;
    top: 158px;
    width: 190px;
    height: 190px;
    border-radius: 50%;
    background: var(--mark-blue);
  }

  .holder {
    position: absolute;
    left: 484px;
    top: 130px;
    margin: 0;
  }
  .holder__name {
    display: block;
    font-weight: 700;
    font-size: 62px;
    line-height: 1;
    letter-spacing: 1px;
    text-transform: uppercase;
  }
  .holder__phone {
    display: block;
    margin-top: 0;
    font-weight: 300;
    font-size: 68px;
    line-height: 1;
    letter-spacing: 1px;
  }

  .brand-name {
    position: absolute;
    left: 67px;
    top: 400px;
    margin: 0;
    font-weight: 400;
    font-size: 47px;
    line-height: 1;
    color: var(--brand-red);
  }

  .contact {
    position: absolute;
    left: 74px;
    top: 536px;
    margin: 0;
    font-style: normal;
    font-weight: 400;
    font-size: 40px;
    line-height: 1;
  }
  .contact__line { display: block; }
  .contact__line + .contact__line { margin-top: 17px; }

  .services {
    position: absolute;
    right: 60px;
    top: 660px;
    margin: 0;
    font-weight: 400;
    font-size: 30px;
    line-height: 1;
    letter-spacing: 1px;
  }
</style>
</head>
<body>
  <main class="card">
    <svg class="card__wave" viewBox="0 0 1200 741" aria-hidden="true">
      <path d="M0,465 C120,560 300,622 480,612 C660,602 820,432 1010,410 C1100,400 1165,410 1200,420 L1200,741 L0,741 Z"/>
    </svg>

    <div class="brand-mark" aria-hidden="true"></div>

    <h1 class="holder">
      <span class="holder__name">Marcus Thornell</span>
      <span class="holder__phone">0427915368</span>
    </h1>

    <p class="brand-name">Keystone Gas &amp; Plumbing</p>

    <address class="contact">
      <span class="contact__line">14 Corrigan Road, Elmvale 3561</span>
      <span class="contact__line">keystoneplumbing@mailbay.com.au</span>
      <span class="contact__line">ABN 52 647 183 925</span>
    </address>

    <p class="services">Domestic &middot; Commercial &middot; Maintenance</p>
  </main>
</body>
</html>
```